I need a flyer for a Car and Bike Show. Please see details and what the flyer info should read on the flyer:

THE Car & Bike Show 2022
Sponsored By Neighbors Backing Dana Corwin & KESLOW'S QUIET-DOWN & CRUISE
Aug. 13, 2022 10am - 6pm
Harlow Creek Park -Ball Field 2470 Brambleton Rd. Union Point, Ga. 30669
Car Entry Fee $15
Admission $5 Children 10 & Under FREE
Contact Trevor Okafor for VENDOR info at (313) 555-0147

I need to have some nice show cars, slingshots, 4-wheelers and bikes on the flyer to make it pop
Please include the attached 3 logos on the flyer

```html
<!DOCTYPE html>
<html lang="en">
<head>
<meta charset="utf-8">
<title>The Car &amp; Bike Show 2022</title>
<link href="https://fonts.googleapis.com/css2?family=Arimo:wght@400;700&display=swap" rel="stylesheet">
<style>
  :root {
    --yellow: #f5f03c;
    --white: #ffffff;
    --navy: #1d3463;
    --navy-deep: #16284f;
    --badge-blue: #3a6cc0;
    --sky: #3f6fb5;
    --rock: #3b3f4e;
    --lava: #e2562a;
  }
  * { margin: 0; padding: 0; box-sizing: border-box; }
  html, body { width: 849px; height: 1200px; overflow: hidden; background: #fff; }
  .flyer {
    position: relative; width: 849px; height: 1200px; overflow: hidden;
    font-family: "Arimo", Arial, sans-serif;
    background: linear-gradient(180deg, var(--navy) 0%, var(--navy-deep) 100%);
  }
  .hero-scene {
    position: absolute; left: 0; top: 0; width: 849px; height: 860px;
    background:
      radial-gradient(ellipse at 30% 75%, rgba(226,86,42,.45), transparent 45%),
      radial-gradient(ellipse at 80% 60%, rgba(226,86,42,.35), transparent 40%),
      linear-gradient(180deg, var(--sky) 0%, #5a6f95 18%, var(--rock) 38%, #2e2f38 100%);
  }
  .wave { position: absolute; left: 0; top: 760px; width: 849px; height: 140px; }
  .vehicle { position: absolute; border-radius: 40px; }
  .vehicle-bike { left: 10px; top: 400px; width: 360px; height: 155px;
    background: linear-gradient(135deg, #c8282c, #b9bcc2 70%, #222); }
  .vehicle-suv { left: 480px; top: 375px; width: 365px; height: 200px;
    background: linear-gradient(160deg, #d8333a, #9c1c22 70%, #333); }
  .vehicle-slingshot { left: 272px; top: 604px; width: 360px; height: 195px;
    background: linear-gradient(150deg, #2a2a30, #d02a30 55%, #1c1c22); }
  .centered { position: absolute; left: 0; width: 849px; text-align: center; }
  .title { top: 28px; font-size: 46px; font-weight: 700; color: var(--yellow); letter-spacing: .5px; }
  .venue { top: 97px; font-size: 17px; font-weight: 700; color: var(--white); }
  .partners { position: absolute; top: 150px; left: 0; width: 849px; display: flex; justify-content: center; gap: 8px; }
  .partner { width: 76px; height: 76px; background: var(--white); display: flex; align-items: center; justify-content: center;
    text-align: center; font-size: 11px; font-weight: 700; color: var(--navy); padding: 4px; line-height: 1.2; }
  .fee-amount { top: 265px; font-size: 38px; font-weight: 700; color: var(--yellow); }
  .fee-label { top: 313px; font-size: 28px; color: var(--yellow); }
  .time-badge { position: absolute; left: 365px; top: 479px; width: 134px; height: 134px; border-radius: 50%;
    background: var(--badge-blue); border: 3px solid var(--white); color: var(--yellow);
    display: flex; flex-direction: column; align-items: center; justify-content: center;
    font-weight: 700; font-size: 23px; line-height: 1.3; }
  .time-badge .to { font-size: 19px; }
  .date { top: 878px; font-size: 38px; font-weight: 700; color: var(--yellow); }
  .admission { position: absolute; top: 932px; left: 122px; font-size: 28px; font-weight: 700; color: var(--yellow); }
  .free-badge { position: absolute; left: 688px; top: 901px; width: 90px; height: 90px; border-radius: 50%;
    background: var(--badge-blue); border: 3px solid var(--white); color: var(--white);
    display: flex; align-items: center; justify-content: center; font-size: 27px; font-weight: 700; }
  .free-badge span { transform: rotate(-22deg); }
  .sponsored-label { top: 1008px; font-size: 16px; color: var(--white); }
  .sponsored-rule { position: absolute; top: 1032px; left: 320px; width: 210px; height: 1px; background: var(--white); }
  .sponsor { font-size: 16px; font-weight: 700; color: var(--yellow); }
  .sponsor-one { top: 1042px; }
  .sponsor-amp { top: 1063px; }
  .sponsor-two { top: 1084px; }
  .contact { top: 1124px; font-size: 18px; font-weight: 700; color: var(--white); }
  .contact em { font-style: normal; color: var(--yellow); }
</style>
</head>
<body>
<main class="flyer">
  <div class="hero-scene" role="img" aria-label="Photo of a glowing lava field under a blue evening sky"></div>
  <div class="vehicle vehicle-bike" role="img" aria-label="Photo of a red and silver sport motorcycle"></div>
  <div class="vehicle vehicle-suv" role="img" aria-label="Photo of a red sport SUV"></div>
  <div class="vehicle vehicle-slingshot" role="img" aria-label="Photo of a black and red three-wheel roadster"></div>

  <svg class="wave" viewBox="0 0 849 140" preserveAspectRatio="none" aria-hidden="true">
    <path d="M0 0 Q424 110 849 0 L849 140 L0 140 Z" fill="#ffffff"/>
    <path d="M0 16 Q424 126 849 16 L849 140 L0 140 Z" fill="#1d3463"/>
  </svg>

  <h1 class="centered title">THE CAR &amp; BIKE SHOW 2022</h1>
  <p class="centered venue">Harlow Creek Park-Ball Field 2470 Brambleton Rd. Union Point,Ga,30669</p>

  <div class="partners">
    <div class="partner">Ridgeline Crew</div>
    <div class="partner">Ironleaf Riders</div>
    <div class="partner">Cedar Lane Motors</div>
  </div>

  <p class="centered fee-amount">$15</p>
  <p class="centered fee-label">Car Entry Fee</p>

  <div class="time-badge"><span>10 AM</span><span class="to">TO</span><span>6 PM</span></div>

  <p class="centered date">Aug. 13, 2022</p>
  <p class="admission">Admission $5 Children 10 &amp; Under</p>
  <div class="free-badge"><span>Free</span></div>

  <p class="centered sponsored-label">Sponsored by</p>
  <div class="sponsored-rule"></div>
  <p class="centered sponsor sponsor-one">Neighbors Backing Dana Corwin</p>
  <p class="centered sponsor sponsor-amp">&amp;</p>
  <p class="centered sponsor sponsor-two">KESLOW'S QUIET-DOWN &amp; CRUISE</p>

  <p class="centered contact">Contact Trevor Okafor for <em>VENDOR</em> info at (313) 555-0147</p>
</main>
</body>
</html>
```